The Timber Loft

We need a business card design for our wardrobe company.
Please visit our website www.zorvelcabinets.com to get an idea of who we are.

```html
<!DOCTYPE html>
<html lang="en">
<head>
<meta charset="utf-8">
<title>The Timber Loft – Business Card</title>
<link rel="stylesheet" href="https://fonts.googleapis.com/css2?family=Montserrat:wght@400;500;600&display=swap">
<style>
  :root {
    --page: #ececec;
    --card: #0d0d0d;
    --card-edge: #1a1a1a;
    --ink: #f2f2f2;
    --ink-soft: #d6d6d6;
    --emboss: #2a2a2a;
    --gold: #b08d57;
  }
  * { margin: 0; padding: 0; box-sizing: border-box; }
  html, body { width: 1200px; height: 800px; overflow: hidden; }
  body {
    background: var(--page);
    font-family: "Montserrat", sans-serif;
    position: relative;
  }
  .card {
    position: absolute;
    width: 540px;
    height: 310px;
    background: var(--card);
    border: 1px solid var(--card-edge);
    border-radius: 3px;
    box-shadow: 0 10px 24px rgba(0,0,0,0.18);
    top: 245px;
  }
  .card--front { left: 40px; }
  .card--back { left: 620px; }

  .brand {
    position: absolute;
    display: flex;
    align-items: center;
    gap: 14px;
  }
  .brand__mark {
    border: 2px solid currentColor;
    flex: none;
  }
  .brand__name {
    font-weight: 600;
    letter-spacing: 0.02em;
    text-transform: uppercase;
    line-height: 1.2;
    white-space: nowrap;
  }
  .brand__tagline {
    font-weight: 600;
    margin-top: 4px;
    white-space: nowrap;
  }

  .card--front .brand {
    color: var(--emboss);
    left: 120px;
    top: 122px;
  }
  .card--front .brand__mark { width: 52px; height: 52px; }
  .card--front .brand__name { font-size: 17px; }
  .card--front .brand__tagline { font-size: 14px; padding-left: 30px; }

  .card--back .brand {
    color: var(--ink);
    left: 32px;
    top: 176px;
  }
  .card--back .brand__mark { width: 40px; height: 40px; }
  .card--back .brand__name { font-size: 11px; }
  .card--back .brand__tagline { font-size: 10px; padding-left: 22px; }

  .contact {
    position: absolute;
    left: 300px;
    top: 56px;
    color: var(--ink);
  }
  .contact__name {
    font-size: 22px;
    font-weight: 400;
    letter-spacing: 0.02em;
  }
  .contact__title {
    font-size: 12px;
    color: var(--gold);
    margin: 2px 0 16px;
  }
  .contact__list { list-style: none; }
  .contact__item {
    display: flex;
    align-items: flex-start;
    gap: 8px;
    font-size: 12px;
    color: var(--ink-soft);
    line-height: 1.45;
    margin-bottom: 4px;
  }
  .contact__icon {
    width: 11px;
    height: 11px;
    flex: none;
    margin-top: 3px;
    fill: var(--gold);
  }
</style>
</head>
<body>
  <section class="card card--front" aria-label="Card front">
    <div class="brand">
      <span class="brand__mark"></span>
      <div class="brand__text">
        <div class="brand__name">The Timber Loft</div>
        <div class="brand__tagline">Built Square and True</div>
      </div>
    </div>
  </section>

  <section class="card card--back" aria-label="Card back">
    <div class="brand">
      <span class="brand__mark"></span>
      <div class="brand__text">
        <div class="brand__name">The Timber Loft</div>
        <div class="brand__tagline">Built Square and True</div>
      </div>
    </div>

    <div class="contact">
      <div class="contact__name">YOUR NAME</div>
      <div class="contact__title">Job Title</div>
      <ul class="contact__list">
        <li class="contact__item">
          <svg class="contact__icon" viewBox="0 0 24 24" aria-hidden="true"><path d="M6.6 10.8a15.1 15.1 0 0 0 6.6 6.6l2.2-2.2c.3-.3.7-.4 1-.2 1.1.4 2.3.6 3.6.6.6 0 1 .4 1 1V20c0 .6-.4 1-1 1A17 17 0 0 1 3 4c0-.6.4-1 1-1h3.5c.6 0 1 .4 1 1 0 1.3.2 2.5.6 3.6.1.3 0 .7-.2 1z"/></svg>
          <span>0207 555 0184</span>
        </li>
        <li class="contact__item">
          <svg class="contact__icon" viewBox="0 0 24 24" aria-hidden="true"><path d="M2 5h20v14H2z M3 6l9 7 9-7" /></svg>
          <span>info@zorvelcabinets.com</span>
        </li>
        <li class="contact__item">
          <svg class="contact__icon" viewBox="0 0 24 24" aria-hidden="true"><path d="M12 2a7 7 0 0 0-7 7c0 5.2 7 13 7 13s7-7.8 7-13a7 7 0 0 0-7-7zm0 9.5A2.5 2.5 0 1 1 12 6.5a2.5 2.5 0 0 1 0 5z"/></svg>
          <span>Harrow Yard, 42 Mill Lane<br>London N4 7QP</span>
        </li>
      </ul>
    </div>
  </section>
</body>
</html>
```